Real Estate Business Cards

Looking for a clean, sharp and professional look for our Real Estate investment Fund that invests in Multi Family Apartment buildings.

Target Market(s)

Real Estate Fund

Industry/Entity Type

Real Estate

Contact Information for Business Card

Company Description: Real Estate Investment Fund
Company Name: RKW Holdings
Name: Marcus Olvane
Cell: (917) 482-0657
Email: marcus@rkwholdings-example.com
Website: www.rkwholdings-example.com
Address: 418, 9th Street, Brooklyn NY 11218

Colors

Designer to choose colors to be used in the design.

Requirements
Nice to have
• Colors to match logo

```html
<!DOCTYPE html>
<html lang="en">
<head>
<meta charset="utf-8">
<title>RKW Holdings – Business Card</title>
<link rel="stylesheet" href="https://fonts.googleapis.com/css2?family=Lato:wght@400;700&display=swap">
<style>
  :root {
    --backdrop: #6f7277;
    --brand-blue: #2f86bf;
    --brand-blue-deep: #236fa3;
    --brand-blue-light: #4ea2d6;
    --card-white: #ffffff;
    --text-grey: #5d6166;
    --text-dark: #4a4d52;
    --watermark: rgba(47, 134, 191, 0.09);
  }
  * { box-sizing: border-box; margin: 0; padding: 0; }
  html, body {
    width: 1200px; height: 912px; overflow: hidden;
    background: var(--backdrop);
    font-family: "Lato", Arial, sans-serif;
  }
  .stage { position: relative; width: 1200px; height: 912px; }

  .card {
    position: absolute; width: 700px; height: 400px;
    overflow: hidden; border-radius: 4px;
    box-shadow: 0 10px 28px rgba(0,0,0,0.35);
  }

  /* Back of card */
  .card--back {
    left: 160px; top: 40px;
    background: linear-gradient(135deg, var(--brand-blue-light) 0%, var(--brand-blue) 55%, var(--brand-blue-deep) 100%);
    display: flex; flex-direction: column; align-items: center; justify-content: center; gap: 18px;
  }
  .back-mark {
    width: 70px; height: 70px; border: 6px solid var(--card-white);
  }
  .back-name {
    color: var(--card-white); font-size: 30px; font-weight: 400; letter-spacing: 2px;
  }

  /* Front of card */
  .card--front {
    left: 340px; top: 472px;
    background: var(--card-white);
  }
  .front-watermark {
    position: absolute; left: 40px; top: 250px;
    width: 250px; height: 250px; background: var(--watermark);
  }
  .brand {
    position: absolute; left: 60px; top: 90px;
    display: flex; flex-direction: column; align-items: flex-start; gap: 16px;
  }
  .brand-mark { width: 64px; height: 64px; border: 6px solid var(--brand-blue); }
  .brand-name {
    color: var(--brand-blue); font-size: 32px; font-weight: 400; letter-spacing: 1px;
  }
  .contact {
    position: absolute; left: 380px; top: 86px;
    color: var(--text-grey);
  }
  .contact-name {
    color: var(--brand-blue); font-size: 25px; font-weight: 700; margin-bottom: 12px;
  }
  .contact-line { font-size: 15px; line-height: 24px; }
  .company {
    margin-top: 22px;
  }
  .company-name { color: var(--text-dark); font-size: 16px; font-weight: 700; line-height: 24px; }
  .company-line { font-size: 16px; line-height: 24px; }
</style>
</head>
<body>
<main class="stage">
  <section class="card card--back" aria-label="Card back">
    <div class="back-mark"></div>
    <div class="back-name">RKW Holdings</div>
  </section>

  <section class="card card--front" aria-label="Card front">
    <div class="front-watermark"></div>
    <div class="brand">
      <div class="brand-mark"></div>
      <div class="brand-name">RKW Holdings</div>
    </div>
    <div class="contact">
      <h1 class="contact-name">Marcus Olvane</h1>
      <p class="contact-line">(917) 482-0657</p>
      <p class="contact-line">marcus@rkwholdings-example.com</p>
      <p class="contact-line">www.rkwholdings-example.com</p>
      <div class="company">
        <p class="company-name">RKW Holdings</p>
        <p class="company-line">Real Estate Investment Fund</p>
        <p class="company-line">418, 9th Street, Brooklyn NY 11218</p>
      </div>
    </div>
  </section>
</main>
</body>
</html>
```